Banner 34"x81"

This is for a Pull Up Banner
I am supplying a sample of my logo and some of my art work for you to incorporate into an upright banner.
Please business name:LuellaRo OpenHarbor Psychotherapy
phone number: 583-214-9067 NOT THE ONE ON THE BUSINESS CARD

```html
<!DOCTYPE html>
<html lang="en">
<head>
<meta charset="utf-8">
<title>LuellaRo OpenHarbor Psychotherapy – Pull Up Banner</title>
<link rel="stylesheet" href="https://fonts.googleapis.com/css2?family=Teko:wght@400;500&family=Ubuntu:wght@300;700&display=swap">
<style>
  :root {
    --page-bg: #eceef0;
    --blue-top: #1f4b92;
    --blue-top-dark: #183f80;
    --blue-base: #11509a;
    --red: #ee3129;
    --cream: #fbdcc4;
    --logo-cream: #f7dcbf;
    --white: #ffffff;
    --photo-dark: #2a1d1a;
    --photo-mid: #4a3a36;
  }
  html, body {
    margin: 0;
    padding: 0;
    width: 1200px;
    height: 1200px;
    overflow: hidden;
    background: var(--page-bg);
  }
  .canvas {
    position: relative;
    width: 1200px;
    height: 1200px;
  }
  .banner {
    position: absolute;
    left: 380px;
    top: 75px;
    width: 441px;
    height: 1050px;
    overflow: hidden;
    background: linear-gradient(160deg, var(--blue-top) 0%, var(--blue-top-dark) 100%);
    box-shadow: 0 6px 18px rgba(0,0,0,0.18);
  }
  .banner-bands {
    position: absolute;
    inset: 0;
    width: 441px;
    height: 1050px;
  }
  .brand-name,
  .brand-tagline {
    position: absolute;
    left: 0;
    width: 100%;
    text-align: center;
    font-family: "Teko", sans-serif;
    font-weight: 400;
    color: var(--logo-cream);
    line-height: 1;
    margin: 0;
  }
  .brand-name {
    top: 56px;
    font-size: 50px;
    letter-spacing: 0.5px;
  }
  .brand-frame {
    position: absolute;
    left: 148px;
    top: 102px;
    width: 160px;
    height: 255px;
    box-sizing: border-box;
    border: 3px solid var(--red);
  }
  .brand-tagline {
    top: 374px;
    font-size: 30px;
  }
  .practice-name {
    position: absolute;
    left: 0;
    top: 492px;
    width: 100%;
    margin: 0;
    text-align: center;
    color: var(--white);
    font-family: "Ubuntu", sans-serif;
    line-height: 1.05;
  }
  .practice-name .practice-owner {
    display: block;
    font-weight: 300;
    font-size: 29px;
  }
  .practice-name .practice-field {
    display: block;
    margin-top: 6px;
    font-weight: 700;
    font-size: 41px;
    letter-spacing: 0.5px;
  }
  .portrait {
    position: absolute;
    left: 136px;
    top: 589px;
    width: 169px;
    height: 251px;
    background: linear-gradient(180deg, var(--photo-dark) 0%, var(--photo-mid) 55%, var(--blue-top) 100%);
  }
  .contact {
    position: absolute;
    left: 0;
    top: 866px;
    width: 100%;
    text-align: center;
    color: var(--white);
  }
  .contact-icons {
    display: flex;
    justify-content: center;
    gap: 19px;
    margin-bottom: 12px;
  }
  .contact-icon {
    width: 30px;
    height: 30px;
    border-radius: 50%;
    background: var(--white);
    display: flex;
    align-items: center;
    justify-content: center;
  }
  .contact-phone {
    font-family: "Teko", sans-serif;
    font-weight: 400;
    font-size: 38px;
    line-height: 1;
    letter-spacing: 0.5px;
    margin: 0;
  }
  .contact-handle {
    font-family: "Teko", sans-serif;
    font-weight: 400;
    font-size: 23px;
    line-height: 1.35;
    margin: 0;
  }
</style>
</head>
<body>
<div class="canvas">
  <div class="banner">
    <svg class="banner-bands" viewBox="0 0 353 840" preserveAspectRatio="none" aria-hidden="true">
      <polygon points="0,308 353,391 353,840 0,840" fill="var(--cream)"/>
      <polygon points="0,385 353,308 353,840 0,840" fill="var(--red)"/>
      <polygon points="0,642 150,655 0,695" fill="var(--white)"/>
      <polygon points="353,565 353,600 170,649" fill="var(--cream)"/>
      <polygon points="0,695 353,600 353,840 0,840" fill="var(--blue-base)"/>
    </svg>

    <p class="brand-name">Luella Ro</p>
    <div class="brand-frame"></div>
    <p class="brand-tagline">Open Harbor</p>

    <h1 class="practice-name">
      <span class="practice-owner">LuellaRo OpenHarbor</span>
      <span class="practice-field">PSYCHOTHERAPY</span>
    </h1>

    <div class="portrait" role="img" aria-label="Portrait photo of the therapist seated on a dark leather sofa"></div>

    <div class="contact">
      <div class="contact-icons">
        <span class="contact-icon">
          <svg width="16" height="16" viewBox="0 0 24 24" aria-hidden="true">
            <path fill="var(--red)" d="M6.6 10.8a15.1 15.1 0 0 0 6.6 6.6l2.2-2.2a1 1 0 0 1 1-.25 11.4 11.4 0 0 0 3.6.57 1 1 0 0 1 1 1V20a1 1 0 0 1-1 1A17 17 0 0 1 3 4a1 1 0 0 1 1-1h3.5a1 1 0 0 1 1 1c0 1.25.2 2.45.57 3.57a1 1 0 0 1-.25 1z"/>
          </svg>
        </span>
        <span class="contact-icon"></span>
        <span class="contact-icon"></span>
      </div>
      <p class="contact-phone">583-214-9067</p>
      <p class="contact-handle">@luellaopenHarbor</p>
      <p class="contact-handle">@luellaharbor</p>
    </div>
  </div>
</div>
</body>
</html>
```